Create a new business card

I’m looking to update my business card to make it match the rest of my brand. I will include my current website as well as what my vehicle designs look like, etc..
What my business currently services
Weekly maintenance pool openings / closings
Equipment repair, including pumps, heaters, salt systems, filters, etc.
We install automatic covers and maintain them as well as provide preventative maintenance

I would like to include my name.
Darren Holcott.
My title
Owner
My email
Darren@tidewellnx.com
4015867120
Www.tidewellnx.com

```html
<!DOCTYPE html>
<html lang="en">
<head>
<meta charset="utf-8">
<title>Tidewell Pool Care – Business Card</title>
<link href="https://fonts.googleapis.com/css2?family=Montserrat:wght@300;400;500;700&display=swap" rel="stylesheet">
<style>
  :root {
    --page-bg: #e6e6e6;
    --sky: #2e9bcd;
    --deep: #1f4a80;
    --navy: #1f3165;
    --aqua: #29b1e6;
    --white: #ffffff;
    --mist: #f4f9fc;
    --mist-blue: #d7ecf7;
  }
  * { box-sizing: border-box; margin: 0; padding: 0; }
  html, body {
    width: 926px; height: 1200px; overflow: hidden;
    background: var(--page-bg);
    font-family: "Montserrat", Arial, sans-serif;
  }
  .canvas { position: relative; width: 926px; height: 1200px; }
  .card {
    position: absolute; top: 357px;
    width: 278px; height: 486px; overflow: hidden;
  }
  .card--front {
    left: 162px;
    background: linear-gradient(180deg, var(--sky) 0%, var(--deep) 100%);
  }
  .card--back { left: 472px; background: var(--white); }

  .artwork {
    position: absolute; left: 16px; top: 24px;
    width: 246px; height: 300px;
    background: linear-gradient(180deg, var(--mist) 0%, var(--mist-blue) 100%);
    display: flex; align-items: center; justify-content: center;
  }
  .brand-mark { display: flex; align-items: center; gap: 8px; }
  .brand-dot {
    width: 14px; height: 14px; border-radius: 50%;
    background: var(--aqua);
  }
  .brand-name {
    font-weight: 700; font-size: 17px; color: var(--navy);
    line-height: 1.15; text-align: left;
  }

  .services {
    position: absolute; left: 0; right: 0; top: 352px;
    list-style: none; text-align: center;
    color: var(--white); font-weight: 500; font-size: 12px;
    line-height: 20px;
  }

  .back-logo {
    position: absolute; left: 0; right: 0; top: 55px; height: 120px;
    display: flex; align-items: center; justify-content: center;
  }
  .back-wave { position: absolute; left: 0; top: 0; width: 278px; height: 486px; }

  .contact {
    position: absolute; left: 60px; top: 320px; color: var(--white);
  }
  .contact__name { font-weight: 700; font-size: 17px; letter-spacing: 0.2px; }
  .contact__title { font-weight: 400; font-size: 13px; }
  .contact__list { list-style: none; margin-top: 14px; font-weight: 300; font-size: 13px; }
  .contact__list li { display: flex; align-items: center; gap: 6px; height: 19.5px; }
  .contact__list svg { width: 11px; height: 11px; flex: none; }
</style>
</head>
<body>
<div class="canvas">
  <section class="card card--front">
    <div class="artwork" role="img" aria-label="Area for the water splash artwork behind the brand name">
      <div class="brand-mark">
        <span class="brand-dot"></span>
        <span class="brand-name">Tidewell<br>Pool Care</span>
      </div>
    </div>
    <ul class="services">
      <li>Pool Opening and closing</li>
      <li>Renovation</li>
      <li>Weekly pool service</li>
      <li>Electronic leak detection</li>
      <li>Equipment repair and upgrades</li>
      <li>Automatic cover installation</li>
    </ul>
  </section>

  <section class="card card--back">
    <div class="back-logo">
      <div class="brand-mark">
        <span class="brand-dot"></span>
        <span class="brand-name">Tidewell<br>Pool Care</span>
      </div>
    </div>
    <svg class="back-wave" viewBox="0 0 278 486" aria-hidden="true">
      <path d="M0 278 C40 215 100 196 150 196 C200 196 250 215 278 238 L278 486 L0 486 Z" fill="var(--aqua)"/>
      <path d="M0 288 C45 230 100 207 152 207 C205 207 250 225 278 246 L278 486 L0 486 Z" fill="var(--navy)"/>
    </svg>
    <div class="contact">
      <h1 class="contact__name">DARREN HOLCOTT</h1>
      <p class="contact__title">Owner</p>
      <ul class="contact__list">
        <li>
          <svg viewBox="0 0 24 24"><path fill="#fff" d="M6.6 10.8a15.1 15.1 0 0 0 6.6 6.6l2.2-2.2c.3-.3.7-.4 1-.2 1.1.4 2.3.6 3.6.6.6 0 1 .4 1 1V20c0 .6-.4 1-1 1A17 17 0 0 1 3 4c0-.6.4-1 1-1h3.5c.6 0 1 .4 1 1 0 1.3.2 2.5.6 3.6.1.3 0 .7-.2 1z"/></svg>
          4015867120
        </li>
        <li>
          <svg viewBox="0 0 24 24"><rect x="2" y="5" width="20" height="14" fill="#fff"/><path d="M2 5l10 8 10-8M2 19l7-7M22 19l-7-7" stroke="var(--navy)" stroke-width="1.6" fill="none"/></svg>
          Darren@tidewellnx.com
        </li>
        <li>
          <svg viewBox="0 0 24 24" fill="none" stroke="#fff" stroke-width="2"><circle cx="12" cy="12" r="10"/><ellipse cx="12" cy="12" rx="4" ry="10"/><path d="M2 12h20M4 7h16M4 17h16"/></svg>
          www.tidewellnx.com
        </li>
      </ul>
    </div>
  </section>
</div>
</body>
</html>
```